New Software Development Firm Needs Stationery

Brindle Works, LLC is a new software development firm specializing in document management and custom engineering applications. We just completed a logo design project on PixelHarbor.

We also have an open project right now on PixelHarbor for business card design. ** We highly encourage you to submit designs to both projects as we want the two designs to have the same look and feel.

Design must be provided for coordinated letterhead and envelopes that works with the selected business card design on the other project.

We want a clean, professional and modern look that works well with our logo. We also require a recommendation for what PC font to use when printing on the new letterhead and envelopes.

The final submission must include source Photoshop or Illustrator files and any fonts used must be specified exactly.

Target Market(s)

Small to medium business professionals - including manufacturers, civil engineering firms, government agencies, architects, as well as general business.

Industry/Entity Type

Software

Requirements
Must have
• Must work very well with logo and business card design. Must work well with a specified and readily-available font on most PCs.
Nice to have
• White letterhead and envelopes are probably preferred, but we're open to suggestions!

```html
<!DOCTYPE html>
<html lang="en">
<head>
<meta charset="utf-8">
<title>Brindle Works – Stationery</title>
<link rel="stylesheet" href="https://fonts.googleapis.com/css2?family=Source+Sans+3:wght@400;600;700&family=Allura&display=swap">
<style>
  :root {
    --bg: #ebebeb;
    --paper: #ffffff;
    --ink: #1a1a1a;
    --text: #444444;
    --muted: #6a6a6a;
    --accent: #d8262f;
    --dark: #3a3a3a;
    --shadow: rgba(0,0,0,0.12);
  }
  * { margin: 0; padding: 0; box-sizing: border-box; }
  html, body { width: 1200px; height: 795px; overflow: hidden; background: var(--bg); }
  body { font-family: "Source Sans 3", Arial, sans-serif; color: var(--text); position: relative; }

  .sheet {
    position: absolute; background: var(--paper);
    box-shadow: 0 2px 10px var(--shadow);
  }

  /* Letterhead */
  .letterhead { left: 90px; top: 40px; width: 506px; height: 715px; padding: 44px 50px 40px 54px; }
  .letterhead .head { display: flex; justify-content: space-between; align-items: flex-end; }
  .wordmark { font-weight: 400; color: var(--ink); letter-spacing: 0.5px; line-height: 1; }
  .letterhead .wordmark { font-size: 34px; }
  .contact { display: grid; grid-template-columns: auto auto; column-gap: 6px; font-size: 7.5px; line-height: 1.3; color: var(--muted); }
  .contact .label { color: var(--accent); text-align: right; }
  .address { font-size: 7.5px; line-height: 1.3; color: var(--muted); }
  .letterhead .details { display: flex; gap: 22px; align-items: flex-start; margin-bottom: 6px; }

  .letter { margin: 64px 0 0 70px; width: 300px; font-size: 8.6px; line-height: 1.45; color: var(--text); }
  .letter .salutation { font-weight: 700; color: var(--ink); margin-bottom: 10px; }
  .letter p { margin-bottom: 11px; }
  .signoff { margin-top: 24px; }
  .signoff .signature { font-family: "Allura", cursive; font-size: 30px; color: var(--ink); line-height: 1; }
  .signoff .role { font-size: 8.6px; font-weight: 700; color: var(--dark); }

  .corner-mark { position: absolute; right: 0; bottom: 60px; }

  /* Business cards */
  .card { width: 340px; height: 194px; left: 690px; }
  .card-front { top: 120px; display: flex; align-items: center; justify-content: center; }
  .card-front .wordmark { font-size: 40px; }

  .card-back { top: 380px; padding: 30px 28px 24px 30px; }
  .card-back .wordmark { font-size: 28px; }
  .card-back .top { display: flex; justify-content: space-between; align-items: flex-start; }
  .card-back .address { font-size: 7.5px; text-align: left; }
  .person { margin-top: 26px; font-size: 12px; color: var(--ink); display: flex; align-items: center; gap: 6px; }
  .person .mark { width: 6px; height: 6px; background: var(--accent); }
  .person .title { font-size: 7.5px; color: var(--muted); letter-spacing: 0.4px; }
  .card-back .contact { margin-top: 8px; font-size: 7.5px; }
</style>
</head>
<body>

<section class="sheet letterhead">
  <header class="head">
    <div class="wordmark">Brindle Works</div>
    <div class="details">
      <div class="contact">
        <span class="label">tel</span><span>(55) 5550 1234</span>
        <span class="label">fax</span><span>(55) 5550 1235</span>
        <span class="label">email</span><span>dana.whitlock@brindleworks.com</span>
        <span class="label">site</span><span>www.brindleworks.com</span>
      </div>
      <div class="address">
        Brindle Works LLC<br>
        Harbor Lane 6, Col. Centro<br>
        The City DF 06100, MX<br>
        12245 The Country
      </div>
    </div>
  </header>

  <article class="letter">
    <p class="salutation">Lorem Ipsum,</p>
    <p>Cras mattis consectetur purus sit amet fermentum. Etiam porta sem malesuada magna mollis euismod. Integer posuere erat a ante venenatis dapibus posuere velit aliquet. Cras justo odio, dapibus ac facilisis in, egestas eget quam. Aenean eu leo quam. Pellentesque ornare sem lacinia quam venenatis vestibulum.</p>
    <p>Vivamus sagittis lacus vel augue laoreet rutrum faucibus dolor auctor. Donec sed odio dui. Etiam porta sem malesuada magna mollis euismod. Morbi leo risus, porta ac consectetur ac, vestibulum at eros. Nullam id dolor id nibh ultricies vehicula ut id elit.</p>
    <p>Donec id elit non mi porta gravida at eget metus. Fusce dapibus, tellus ac cursus commodo, tortor mauris condimentum nibh, ut fermentum massa justo sit amet risus. Cras justo odio, dapibus ac facilisis in, egestas eget quam. Cum sociis natoque penatibus et magnis dis parturient montes, nascetur ridiculus mus.</p>
    <p>Cum sociis natoque penatibus et magnis dis parturient montes, nascetur ridiculus mus. Curabitur blandit tempus porttitor. Aenean lacinia bibendum nulla sed consectetur. Lorem ipsum dolor sit amet, consectetur adipiscing elit.</p>
    <p>Cras justo odio, dapibus ac facilisis in, egestas eget quam. Morbi leo risus, porta ac consectetur ac, vestibulum at eros. Duis mollis, est non commodo luctus, nisi erat porttitor ligula, eget lacinia odio sem nec elit. Integer posuere erat a ante venenatis dapibus posuere velit aliquet. Vivamus sagittis lacus vel augue laoreet rutrum faucibus dolor auctor.</p>
    <div class="signoff">
      <div class="signature">Your Name</div>
      <div class="role">Company Director</div>
    </div>
  </article>

  <svg class="corner-mark" width="16" height="16" viewBox="0 0 16 16" aria-hidden="true">
    <polygon points="0,16 16,0 16,16" fill="var(--dark)"/>
    <polygon points="0,16 16,0 0,0" fill="var(--accent)"/>
  </svg>
</section>

<section class="sheet card card-front">
  <div class="wordmark">Brindle Works</div>
</section>

<section class="sheet card card-back">
  <div class="top">
    <div class="wordmark">Brindle Works</div>
    <div class="address">
      Brindle Works LLC<br>
      Harbor Lane 6, Col. Centro<br>
      The City DF 06100, MX<br>
      12245 The Country
    </div>
  </div>
  <div class="person">
    <span class="mark"></span>
    <span>Dana Whitlock</span>
    <span class="title">| MANAGER</span>
  </div>
  <div class="contact">
    <span class="label">tel</span><span>(55) 5550 1234</span>
    <span class="label">fax</span><span>(55) 5550 1235</span>
    <span class="label">email</span><span>dana.whitlock@brindleworks.com</span>
    <span class="label">site</span><span>www.brindleworks.com</span>
  </div>
</section>

</body>
</html>
```